bramblegate crest roofing flyer*

I need an a5 size flyer designing to go in our local advertising magazine.We are based in the north west of England Id like key features from the website including on the flyer, possibly even reviews, what we do ect.I don't however want it too busy, simple pictures and description of service.company colours and logo. I require simple one sided business cards toonumber, web address and logowinner will receive a request to design around 5 different double sided a5 flyers too, each with all our services on one side and the other primarily for one service we have provided locally with a spacve to put the house number down.REPAIRSROOFLINEFLAT ROOFS PITCHED ROOFSSYNTHETIC ROOFSUP TO 50 YEARS WARRANTY AVAILABLERANKED THE #1 FLAT ROOFER IN THE UK OUT OF 787 REGISTERED FLAT ROOFING COMPANIESRANKED THE #10 ROOFING COMPANY IN THE UK OUT OF 1976 REGISTERED SPECIALIST ROOFING COMPANIESBOTH FOR COST, CUSTOMER SERVICE AND QUALITY WITH 5 STAR REVIEWSGUARANTEED TO FIND AND FIX A LEAKAPPROVED INSTALLERSAWARD WINNINGTIME SERVED FIXED PRICES

Target Market(s)

homeowners

Colors

Designer to choose only greyscale colors for use in the design.

Requirements
Must have
• contact details
• pictures of my work
• clear and simple

```html
<!DOCTYPE html>
<html lang="en">
<head>
<meta charset="utf-8">
<title>Bramblegate Crest Roofing – Flyer</title>
<link href="https://fonts.googleapis.com/css2?family=Oswald:wght@400;500;700&family=Open+Sans:wght@400;700&display=swap" rel="stylesheet">
<style>
  :root {
    --green-mid: #43963f;
    --green-light: #72bf44;
    --green-dark: #0e8441;
    --green-tick: #137a3c;
    --white: #ffffff;
  }
  html, body { margin: 0; padding: 0; overflow: hidden; }
  body { width: 839px; height: 1200px; background: var(--white); }
  .flyer {
    position: relative; width: 839px; height: 1200px; overflow: hidden;
    background: var(--white); font-family: "Open Sans", sans-serif;
  }
  .flyer__backdrop { position: absolute; inset: 0; }
  .brand {
    position: absolute; left: 86px; top: 66px; width: 667px;
    font-family: "Oswald", sans-serif; font-weight: 700; color: var(--green-mid);
    text-transform: uppercase; line-height: 1;
  }
  .brand__line1 { display: block; font-size: 64px; letter-spacing: 1px; white-space: nowrap; }
  .brand__line2 {
    display: block; font-size: 80px; letter-spacing: 18px; text-align: right;
    margin-top: 63px; margin-right: -18px; white-space: nowrap;
  }
  .headline {
    position: absolute; left: 98px; top: 362px; margin: 0;
    font-family: "Oswald", sans-serif; font-weight: 500; font-size: 68px;
    color: var(--white); letter-spacing: 0.5px; line-height: 1;
    transform: rotate(-2.7deg); transform-origin: left top; white-space: nowrap;
  }
  .intro {
    position: absolute; left: 84px; top: 716px; width: 660px; margin: 0;
    color: var(--white); font-size: 20.5px; line-height: 29px;
  }
  .credentials {
    position: absolute; left: 52px; top: 818px; margin: 0; padding: 0; list-style: none;
    font-family: "Oswald", sans-serif; font-weight: 500; font-size: 28px; color: var(--white);
  }
  .credentials li { display: flex; align-items: center; height: 48px; }
  .credentials svg { width: 32px; height: 28px; margin-right: 6px; flex: none; }
  .contact {
    position: absolute; left: 0; top: 990px; width: 839px; text-align: center; color: var(--white);
  }
  .contact__phone {
    display: flex; justify-content: center; align-items: center; gap: 8px; padding-left: 20px;
    font-family: "Oswald", sans-serif; font-weight: 500; font-size: 84px; line-height: 1;
  }
  .contact__phone svg { width: 26px; height: 34px; margin-top: 32px; }
  .contact__web {
    display: flex; justify-content: center; align-items: center; gap: 12px; margin-top: 8px;
    font-weight: 700; font-size: 29px; padding-left: 50px;
  }
  .contact__web svg { width: 26px; height: 26px; }
  .tagline {
    position: absolute; left: 0; top: 1120px; width: 839px; text-align: center; margin: 0;
    font-family: "Oswald", sans-serif; font-weight: 500; font-size: 31px; color: var(--green-light);
    line-height: 1;
  }
</style>
</head>
<body>
<div class="flyer">
  <svg class="flyer__backdrop" width="839" height="1200" viewBox="0 0 839 1200">
    <defs>
      <linearGradient id="houseTones" x1="0" y1="0" x2="0" y2="1">
        <stop offset="0" stop-color="#5a5b5e"/>
        <stop offset="0.3" stop-color="#6d6a66"/>
        <stop offset="0.4" stop-color="#b8a07a"/>
        <stop offset="0.85" stop-color="#a98f68"/>
        <stop offset="1" stop-color="#4d4e50"/>
      </linearGradient>
    </defs>
    <polygon points="0,440 839,410 839,672 0,708" fill="url(#houseTones)" role="img" aria-label="Photograph of a stone terraced house with a newly finished slate roof"/>
    <polygon points="0,356 839,318 839,424 0,460" fill="var(--green-mid)"/>
    <polygon points="0,708 839,670 839,958 0,994" fill="var(--green-light)"/>
    <polygon points="0,994 839,958 839,1200 0,1200" fill="var(--green-dark)"/>
  </svg>

  <div class="brand">
    <span class="brand__line1">Bramblegate Crest</span>
    <span class="brand__line2">Roofing</span>
  </div>

  <h1 class="headline">READY FOR A NEW ROOF?</h1>

  <p class="intro">We treat every job as a showcase of our ability and will complete the job with great care and always take our time to do it properly at a fair price.</p>

  <ul class="credentials">
    <li><svg viewBox="0 0 32 28"><path d="M2 16 L11 26 L30 2 L11 20 Z" fill="var(--green-tick)"/></svg>Ranked #1 in the UK for Cost, Customer Service and Quality.</li>
    <li><svg viewBox="0 0 32 28"><path d="M2 16 L11 26 L30 2 L11 20 Z" fill="var(--green-tick)"/></svg>12th in the UK out of 1979 registered roofing companies</li>
    <li><svg viewBox="0 0 32 28"><path d="M2 16 L11 26 L30 2 L11 20 Z" fill="var(--green-tick)"/></svg>1st in the UK out of 768 flat roofing specialists</li>
  </ul>

  <div class="contact">
    <div class="contact__phone">
      <svg viewBox="0 0 26 34"><path d="M6 2 L11 1 L13 9 L9 11 Q10 19 15 24 L18 21 L24 26 L21 31 Q8 30 3 12 Q3 5 6 2 Z" fill="var(--green-light)"/></svg>
      <span>07700900318</span>
    </div>
    <div class="contact__web">
      <svg viewBox="0 0 26 26" fill="none" stroke="var(--green-light)" stroke-width="1.8">
        <circle cx="13" cy="13" r="11"/><ellipse cx="13" cy="13" rx="5" ry="11"/>
        <line x1="2" y1="13" x2="24" y2="13"/><line x1="4" y1="7" x2="22" y2="7"/><line x1="4" y1="19" x2="22" y2="19"/>
      </svg>
      <span>bramblegatecrestroofing.com</span>
    </div>
  </div>

  <p class="tagline">CALL US FOR ANY ROOFLINE REPLACEMENTS AT ANY HEIGHT</p>
</div>
</body>
</html>
```